Potato chips bag design of 85 gram for Greek and East Europe market

I want a new design for a new potato chips bag for the Greek market. The product is going to be all natural ingredient, gluten free, preservatives free, allergen free from Greek organic potatoes . Thick cut, marinated potatoes that are premium vs others. For packaging we want it to stand out on shelf. Have a Matt film . It will be called Silverbrook Tumble. Salt and Oregano flavors to start with.
Ideally to stand out on shelf we were thinking to have a black/white Color pallet and have an artistic pattern printed like the pictures attached. But of course open to ideas.
Target Market(s)
Greece and East Europe
Industry/Entity Type
Snacks Packaged goods
Requirements
Must have
- Matt film that stands out on shelf . 85 grams bag so 25cm tall and 15 cms length
Nice to have
- Ideally black/white pallet as it looks more premium. Patterns artistic that will make it look like art.
Should not have
- Traditional Pevo type of design (red-green colors etc)

```html
<!DOCTYPE html>
<html lang="en">
<head>
<meta charset="utf-8">
<title>Silverbrook Tumble – Salt and Oregano 85 gms</title>
<link rel="stylesheet" href="https://fonts.googleapis.com/css2?family=Anton&family=Roboto+Condensed:wght@700;800&display=swap">
<style>
  :root {
    --ink: #0b0b0b;
    --ink-soft: #2a2a2a;
    --paper: #ffffff;
    --cream: #f2efe8;
    --stage: #ffffff;
  }
  html, body {
    margin: 0;
    padding: 0;
    width: 1200px;
    height: 1200px;
    overflow: hidden;
    background: var(--stage);
  }
  .canvas {
    position: relative;
    width: 1200px;
    height: 1200px;
  }
  .bag-front {
    position: absolute;
    left: 258px;
    top: 100px;
    width: 684px;
    height: 1000px;
    overflow: hidden;
    background: var(--ink);
  }
  .wave-pattern {
    position: absolute;
    inset: 0;
    background:
      repeating-linear-gradient(172deg, transparent 0 38px, rgba(242,239,232,0.10) 38px 44px, transparent 44px 70px),
      radial-gradient(ellipse at 30% 20%, #3a3a3a 0%, transparent 55%),
      radial-gradient(ellipse at 70% 80%, #333 0%, transparent 55%),
      linear-gradient(180deg, #1c1c1c, #0b0b0b 50%, #1c1c1c);
  }
  .weight-badge {
    position: absolute;
    left: 376px;
    top: 46px;
    width: 88px;
    height: 88px;
    border-radius: 50%;
    background: var(--paper);
    color: var(--ink);
    display: flex;
    flex-direction: column;
    align-items: center;
    justify-content: center;
    transform: rotate(-8deg);
    font-family: "Roboto Condensed", sans-serif;
    font-weight: 800;
    line-height: 0.9;
  }
  .weight-badge .amount { font-size: 34px; letter-spacing: 1px; }
  .weight-badge .unit { font-size: 24px; }
  .label-block {
    position: absolute;
    left: 100px;
    top: 240px;
    width: 460px;
    transform: rotate(-8deg);
    transform-origin: left top;
    color: var(--paper);
  }
  .brand-top {
    display: block;
    margin-left: 110px;
    font-family: "Roboto Condensed", sans-serif;
    font-weight: 800;
    font-size: 46px;
    line-height: 1;
    letter-spacing: -1px;
    text-shadow: 0 0 6px var(--ink);
  }
  .brand-main {
    display: block;
    font-family: "Anton", sans-serif;
    font-size: 150px;
    line-height: 0.95;
    letter-spacing: -2px;
    color: var(--cream);
    text-shadow: 0 0 10px var(--ink);
  }
  .flavour {
    display: block;
    margin-left: 140px;
    font-family: "Roboto Condensed", sans-serif;
    font-weight: 800;
    font-size: 38px;
    line-height: 1.05;
    text-shadow: 0 0 6px var(--ink);
  }
  .claims {
    list-style: none;
    margin: 14px 0 0 84px;
    padding: 0;
    font-family: "Roboto Condensed", sans-serif;
    font-weight: 800;
    font-size: 36px;
    line-height: 1.18;
  }
  .claims li {
    display: flex;
    align-items: center;
    gap: 14px;
    width: max-content;
    padding: 0 8px;
    background: var(--ink);
  }
  .claims li::before {
    content: "";
    width: 20px;
    height: 20px;
    background: var(--paper);
    flex: none;
  }
</style>
</head>
<body>
  <main class="canvas">
    <section class="bag-front">
      <div class="wave-pattern" role="img" aria-label="Artistic black and white flowing wave line pattern covering the bag"></div>

      <div class="weight-badge">
        <span class="amount">85</span>
        <span class="unit">gms</span>
      </div>

      <div class="label-block">
        <span class="brand-top">Silverbrook</span>
        <span class="brand-main">Tumble</span>
        <span class="flavour">Salt and Oregano</span>
        <ul class="claims">
          <li>Natural Ingredient</li>
          <li>Gluten Free</li>
          <li>Preservatives Free</li>
          <li>Allergen Free</li>
        </ul>
      </div>
    </section>
  </main>
</body>
</html>
```